Worksheet for a seminar - wheel of wellbeing

I need a 1 page worksheet for a course I am running next week.
1. The worksheet is based is designed to tie into Dorvelle who use 4 colours per specific quadrants - Blue top left, Yellow top right, Green bottom left, Red bottom right. As this is designed to be written and to be printed, it may need to be pale colours however I am open to the correct colours with the image on top if necessary

2. The wellbeing wheel needs to be a design of it's own as it will be used in other things. I would like to have a format for the base wheel that can be changed by me (Only the title names)

3. I have provided the 2 business logo's - these down need to be too big

I hope this helps.

Corporate managers and staff - worksheet being used in a workshop

Wheel

• A professional looking wheel that can be used for other purposes. I want to be able to change the 'pie' titles. I will also require a A4 size of the wheel with blank spaces for titles
• A modern feel

```html
<!DOCTYPE html>
<html lang="en">
<head>
<meta charset="utf-8">
<title>Wheel of Wellbeing – Worksheet</title>
<link href="https://fonts.googleapis.com/css2?family=Montserrat:wght@700;800&family=Raleway:wght@300;400;500&family=Roboto+Slab:wght@700&display=swap" rel="stylesheet">
<style>
  :root{
    --ink:#58595b;
    --ink-soft:#4d4d4d;
    --blue:#0a93d2;   --blue-pale:#e6eff8;
    --yellow:#fff200; --yellow-pale:#fefbe1;
    --green:#3ab54a;  --green-pale:#eff4e1;
    --red:#f05a48;    --red-pale:#f6e2da;
    --seg-business:#16a0db; --seg-physical:#f6c412; --seg-emotional:#8dc63f;
    --seg-spiritual:#f68121; --seg-love:#3aaa49; --seg-family:#e3202a;
    --seg-social:#92278f; --seg-personal:#c39a6b;
    --spoke:#8a8a8a;
    --brand:#3aa86b;
  }
  *{margin:0;padding:0;box-sizing:border-box}
  html,body{width:849px;height:1200px;overflow:hidden;background:#fff}
  body{position:relative;font-family:"Raleway",sans-serif;color:var(--ink)}
  .abs{position:absolute}

  .sheet-title{left:0;width:849px;top:56px;text-align:center;font:800 42px/1 "Montserrat",sans-serif;letter-spacing:2px;color:var(--ink)}
  .sheet-subtitle{left:0;width:849px;top:111px;text-align:center;font:400 16px/1 "Raleway",sans-serif;letter-spacing:5px;color:#333}

  .panel-head{height:67px}
  .head-assess{left:47px;top:155px;width:379px;background:var(--blue);border-top-left-radius:30px}
  .head-goals{left:437px;top:155px;width:379px;background:var(--yellow);border-top-right-radius:30px}
  .head-action{left:47px;top:649px;width:379px;background:var(--green)}
  .head-reflect{left:437px;top:649px;width:379px;background:var(--red)}
  .body-assess{left:47px;top:222px;width:379px;height:417px;background:var(--blue-pale)}
  .body-goals{left:437px;top:222px;width:379px;height:417px;background:var(--yellow-pale)}
  .body-action{left:47px;top:716px;width:379px;height:377px;background:var(--green-pale);border-bottom-left-radius:36px}
  .body-reflect{left:437px;top:716px;width:379px;height:377px;background:var(--red-pale);border-bottom-right-radius:36px}

  .step{position:absolute;right:58px;top:15px;text-align:right}
  .step-title{font:800 19px/1 "Montserrat",sans-serif;color:#fff}
  .step-sub{font:300 13px/1 "Raleway",sans-serif;color:#fff;margin-top:7px}
  .head-goals .step{right:29px}
  .head-goals .step-title{color:var(--ink-soft)}
  .head-goals .step-sub{color:var(--ink-soft)}
  .head-reflect .step{right:29px}
  .head-action .step{top:17px}
  .head-reflect .step{top:17px}
  .step-icon{position:absolute;left:20px;top:14px}
  .head-goals .step-icon{left:22px;top:10px}

  .wheel{width:350px;height:350px}
  .wheel-assess{left:62px;top:241px}
  .wheel-goals{left:455px;top:241px}
  .wheel-label{font:700 7.6px "Roboto Slab",serif;fill:#fff;letter-spacing:.3px}
  .scale-num{font:400 7px "Raleway",sans-serif;fill:#555}

  .caption{width:379px;text-align:center;font:400 11.5px/1 "Raleway",sans-serif;color:#333}
  .caption-assess{left:47px;top:610px}
  .caption-goals{left:437px;top:610px}

  .hub{left:394px;top:606px;width:72px;height:72px;border-radius:50%;background:#fff}

  .col-label{font:400 11.5px/1 "Raleway",sans-serif;color:#333}
  .action-row{left:71px;width:330px;height:60px;background:#fff;border-radius:8px}
  .action-row::after{content:"";position:absolute;left:253px;top:0;bottom:0;width:2px;background:var(--green-pale)}

  .question{left:456px;font:400 11.5px/1 "Raleway",sans-serif;color:#333}
  .answer{left:455px;width:340px;height:49px;background:#fff;border-radius:7px}

  .brand{display:flex;align-items:center;gap:6px;font:700 14px/1 "Montserrat",sans-serif;color:var(--brand);white-space:nowrap}
  .brand-dot{width:11px;height:11px;border-radius:50%;background:var(--brand)}
  .brand-wellness{left:486px;top:1140px}
  .brand-growth{right:33px;top:1140px}
</style>
</head>
<body>

<h1 class="abs sheet-title">WHEEL OF WELLBEING</h1>
<p class="abs sheet-subtitle">A WHOLE BRAIN APPROACH</p>

<header class="abs panel-head head-assess">
  <svg class="step-icon" width="60" height="42" viewBox="0 0 60 42" aria-hidden="true">
    <g fill="none" stroke="#fff" stroke-width="3" stroke-linecap="round" stroke-linejoin="round">
      <line x1="30" y1="3" x2="30" y2="10"/>
      <line x1="10" y1="14" x2="50" y2="10"/>
      <path d="M10 14 L3 30 H17 Z"/><path d="M50 10 L43 26 H57 Z"/>
    </g>
    <circle cx="30" cy="12" r="4" fill="#fff"/>
    <path d="M3 31 Q10 37 17 31 Z M43 27 Q50 33 57 27 Z" fill="#fff"/>
  </svg>
  <div class="step"><div class="step-title">1. ASSESS</div><div class="step-sub">Where are you now?</div></div>
</header>
<section class="abs body-assess"></section>

<header class="abs panel-head head-goals">
  <svg class="step-icon" width="44" height="50" viewBox="0 0 44 50" aria-hidden="true">
    <path d="M26 2a10 10 0 0 1 10 10c0 8-10 18-10 18S16 20 16 12A10 10 0 0 1 26 2z" fill="#fff"/>
    <circle cx="26" cy="12" r="4" fill="var(--yellow)"/>
    <path d="M24 32 C10 32 4 38 12 42 C18 45 10 48 4 48 H40 C44 44 30 42 26 38 C22 35 30 33 24 32Z" fill="#fff"/>
  </svg>
  <div class="step"><div class="step-title">3. SET GOALS</div><div class="step-sub">Where do you want to be?</div></div>
</header>
<section class="abs body-goals"></section>

<svg class="abs wheel wheel-assess" viewBox="-175 -175 350 350" role="img" aria-label="Wheel of wellbeing scored 1 to 10">
  <defs>
    <path id="label-track" d="M -156 0 A 156 156 0 1 1 156 0 A 156 156 0 1 1 -156 0"/>
    <g id="spoke">
      <line x1="-135" y1="0" x2="135" y2="0" stroke="var(--spoke)" stroke-width=".8"/>
      <g stroke="var(--spoke)" stroke-width=".8">
        <line x1="13" y1="-2" x2="13" y2="2"/><line x1="26" y1="-2" x2="26" y2="2"/>
        <line x1="39" y1="-2" x2="39" y2="2"/><line x1="52" y1="-2" x2="52" y2="2"/>
        <line x1="78" y1="-2" x2="78" y2="2"/><line x1="91" y1="-2" x2="91" y2="2"/>
        <line x1="104" y1="-2" x2="104" y2="2"/><line x1="117" y1="-2" x2="117" y2="2"/>
        <line x1="-13" y1="-2" x2="-13" y2="2"/><line x1="-26" y1="-2" x2="-26" y2="2"/>
        <line x1="-39" y1="-2" x2="-39" y2="2"/><line x1="-52" y1="-2" x2="-52" y2="2"/>
        <line x1="-78" y1="-2" x2="-78" y2="2"/><line x1="-91" y1="-2" x2="-91" y2="2"/>
        <line x1="-104" y1="-2" x2="-104" y2="2"/><line x1="-117" y1="-2" x2="-117" y2="2"/>
      </g>
      <g stroke="#444" stroke-width="1.6">
        <line x1="65" y1="-4" x2="65" y2="4"/><line x1="130" y1="-5" x2="130" y2="5"/>
        <line x1="-65" y1="-4" x2="-65" y2="4"/><line x1="-130" y1="-5" x2="-130" y2="5"/>
      </g>
      <text class="scale-num" x="65" y="-7" text-anchor="middle">5</text>
      <text class="scale-num" x="130" y="-8" text-anchor="middle">10</text>
      <text class="scale-num" x="-65" y="13" text-anchor="middle" transform="rotate(180 -65 10)">5</text>
      <text class="scale-num" x="-130" y="14" text-anchor="middle" transform="rotate(180 -130 11)">10</text>
    </g>
    <g id="wheel-base">
      <circle r="170" fill="#fff"/>
      <g fill="none" stroke-width="26">
        <path d="M -108.37 -112.22 A 156 156 0 0 1 -2.72 -155.98" stroke="var(--seg-business)"/>
        <path d="M 2.72 -155.98 A 156 156 0 0 1 108.37 -112.22" stroke="var(--seg-physical)"/>
        <path d="M 112.22 -108.37 A 156 156 0 0 1 155.98 -2.72" stroke="var(--seg-emotional)"/>
        <path d="M 155.98 2.72 A 156 156 0 0 1 112.22 108.37" stroke="var(--seg-spiritual)"/>
        <path d="M 108.37 112.22 A 156 156 0 0 1 2.72 155.98" stroke="var(--seg-love)"/>
        <path d="M -2.72 155.98 A 156 156 0 0 1 -108.37 112.22" stroke="var(--seg-family)"/>
        <path d="M -112.22 108.37 A 156 156 0 0 1 -155.98 2.72" stroke="var(--seg-social)"/>
        <path d="M -155.98 -2.72 A 156 156 0 0 1 -112.22 -108.37" stroke="var(--seg-personal)"/>
      </g>
      <g class="wheel-label" dominant-baseline="central" text-anchor="middle">
        <text><textPath href="#label-track" startOffset="6.25%">PERSONAL GROWTH</textPath></text>
        <text><textPath href="#label-track" startOffset="18.75%">BUSINESS/CAREER/STUDY</textPath></text>
        <text><textPath href="#label-track" startOffset="31.25%">PHYSICAL HEALTH</textPath></text>
        <text><textPath href="#label-track" startOffset="43.75%">EMOTIONAL HEALTH</textPath></text>
        <text><textPath href="#label-track" startOffset="56.25%">SPIRITUAL</textPath></text>
        <text><textPath href="#label-track" startOffset="68.75%">LOVE &amp; RELATIONSHIPS</textPath></text>
        <text><textPath href="#label-track" startOffset="81.25%">FAMILY</textPath></text>
        <text><textPath href="#label-track" startOffset="93.75%">SOCIAL/COMMUNITY</textPath></text>
      </g>
      <use href="#spoke" transform="rotate(-112.5)"/>
      <use href="#spoke" transform="rotate(-67.5)"/>
      <use href="#spoke" transform="rotate(-22.5)"/>
      <use href="#spoke" transform="rotate(22.5)"/>
    </g>
  </defs>
  <use href="#wheel-base"/>
</svg>
<svg class="abs wheel wheel-goals" viewBox="-175 -175 350 350" role="img" aria-label="Wheel of wellbeing for goal setting">
  <use href="#wheel-base"/>
</svg>

<p class="abs caption caption-assess">Assess each area from 1-10 (1= lousy/10=Awesome!)</p>
<p class="abs caption caption-goals">Assess each area from 1-10 (1= lousy/10=Awesome!)</p>

<header class="abs panel-head head-action">
  <svg class="step-icon" width="44" height="44" viewBox="0 0 44 44" aria-hidden="true">
    <path d="M38 4 C26 4 16 12 12 24 L20 32 C32 28 40 18 38 4Z" fill="#fff"/>
    <circle cx="28" cy="15" r="4" fill="var(--green)"/>
    <path d="M12 24 L4 24 L12 16 L18 16Z M20 32 L20 40 L28 32 L28 26Z M10 30 L4 40 L14 34Z" fill="#fff"/>
  </svg>
  <div class="step"><div class="step-title">4. ACTION PLAN</div><div class="step-sub">What do you need to do?</div></div>
</header>
<section class="abs body-action"></section>
<span class="abs col-label" style="left:149px;top:751px">Action</span>
<span class="abs col-label" style="left:346px;top:746px">Date by</span>
<div class="abs action-row" style="top:774px"></div>
<div class="abs action-row" style="top:847px"></div>
<div class="abs action-row" style="top:920px"></div>
<div class="abs action-row" style="top:993px"></div>

<header class="abs panel-head head-reflect">
  <svg class="step-icon" width="46" height="44" viewBox="0 0 46 44" aria-hidden="true">
    <path d="M10 26 a8 8 0 0 1 0-16 a10 10 0 0 1 18-4 a9 9 0 0 1 12 8 a7 7 0 0 1-2 12Z" fill="#fff"/>
    <circle cx="22" cy="32" r="4" fill="#fff"/><circle cx="30" cy="39" r="2.6" fill="#fff"/>
  </svg>
  <div class="step"><div class="step-title">2. REFLECT ON RESULTS</div><div class="step-sub">How do you feel about where you are at?</div></div>
</header>
<section class="abs body-reflect"></section>
<p class="abs question" style="top:745px">Are there any surpises on your wheel?</p>
<div class="abs answer" style="top:763px"></div>
<p class="abs question" style="top:826px">What wellbeing gaps stand out as being important?</p>
<div class="abs answer" style="top:847px"></div>
<p class="abs question" style="top:914px">How do you feel about it?</p>
<div class="abs answer" style="top:930px"></div>
<p class="abs question" style="top:998px">How might this affect your homelife/worklife?</p>
<div class="abs answer" style="top:1014px"></div>

<div class="abs hub">
  <svg width="72" height="72" viewBox="0 0 72 72" aria-hidden="true">
    <g stroke="#bdbdbd" stroke-width="2.4" stroke-linecap="round" fill="none">
      <line x1="20" y1="20" x2="52" y2="52"/><line x1="52" y1="20" x2="20" y2="52"/>
      <polyline points="20,44 20,52 28,52"/><polyline points="52,44 52,52 44,52"/>
    </g>
  </svg>
</div>

<div class="abs brand brand-wellness"><span class="brand-dot"></span>Fieldmark Wellness</div>
<div class="abs brand brand-growth">Northbay Growth</div>

</body>
</html>
```